Stationery Design Project - New innovative law firm

I need a simple design, yet the tone of the stationery set need to express modern, professionalism, smart and forward-thinking. I don’t need a business card, but require the stationery set to have:
• Design letterhead
• Design facsimile
• Design memo
The triangular logo with Corvane Associates words etc, need to be present in the stationery. The red triangular logo should not be re-designed, but feel free to play around with the placement and colours of the Corvane Associates words etc....?

Target Market(s)

Business clients

Industry/Entity Type

Business

Requirements
Must have
• The triangular logo with Corvane Associates words etc...for branding.

```html
<!DOCTYPE html>
<html lang="en">
<head>
<meta charset="utf-8">
<title>Corvane Associates Stationery Set</title>
<link rel="stylesheet" href="https://fonts.googleapis.com/css2?family=Open+Sans:wght@400;600;700&display=swap">
<style>
:root{
  --backdrop:#4e3322;
  --paper:#ffffff;
  --paper-fax:#f3f3f3;
  --brand-red:#d3141c;
  --brand-dark:#1b1b1b;
  --ink:#333333;
  --ink-soft:#8a8a8a;
  --rule:#b9b9b9;
  --label:#f2ece6;
}
*{margin:0;padding:0;box-sizing:border-box}
html,body{width:1200px;height:297px;overflow:hidden}
body{background:var(--backdrop);font-family:"Open Sans",Arial,sans-serif;position:relative;color:var(--ink)}
.sheet{position:absolute;top:27px;width:172px;height:228px;background:var(--paper);overflow:hidden;box-shadow:0 2px 5px rgba(0,0,0,.45)}
.sheet--fax{background:var(--paper-fax)}
.sheet--letter-1{left:18px}.sheet--letter-2{left:207px}.sheet--fax{left:400px}
.sheet--memo-1{left:598px}.sheet--memo-2{left:795px}.sheet--memo-3{left:990px}
.sheet-label{position:absolute;top:260px;width:172px;text-align:center;font-size:14px;color:var(--label);font-weight:400}
.header-art,.footer-art{position:absolute;left:0;width:172px;display:block}
.header-art{top:0;height:40px}
.footer-art{bottom:0;height:8px}
.brand{position:absolute;left:14px;top:31px;display:flex;align-items:center;gap:2px;font-size:6.2px;font-weight:700;color:var(--brand-dark);letter-spacing:.1px;white-space:nowrap}
.brand-square{width:5px;height:5px;background:var(--brand-red)}
.partners{position:absolute;right:6px;top:4px;text-align:right;font-size:2.6px;line-height:3.6px;color:#fff;font-weight:600}
.sheet--memo-3 .partners{color:var(--brand-red)}
.ref{position:absolute;right:14px;top:42px;font-size:2.8px;font-weight:700;color:var(--brand-dark)}
.tiny{font-size:2.6px;line-height:3.5px;color:var(--ink)}
.block{position:absolute;left:14px;right:16px}
.para{margin-bottom:3.5px;color:#666}
.signoff{position:absolute;left:14px;top:186px}
.office{position:absolute;right:8px;bottom:12px;text-align:right;font-size:2.2px;line-height:3px;color:var(--ink-soft)}
.web{position:absolute;right:6px;bottom:1.5px;font-size:2.4px;color:#fff;font-weight:600}
.fax-title{position:absolute;left:14px;top:44px;font-size:11px;font-weight:400;color:var(--brand-dark)}
.fax-grid{position:absolute;left:14px;top:62px;width:146px;display:grid;grid-template-columns:1fr 1fr;column-gap:6px;row-gap:3px}
.fax-field{display:flex;gap:3px;font-size:2.7px;border-bottom:.4px solid var(--rule);padding-bottom:.6px}
.fax-field b{width:12px;font-weight:600}
.fax-checks{position:absolute;left:14px;top:95px;display:flex;gap:5px;font-size:2.6px}
.fax-checks span::before{content:"";display:inline-block;width:2.6px;height:2.6px;border:.4px solid var(--ink);margin-right:1px;vertical-align:-.4px}
.fax-greeting{position:absolute;left:14px;top:104px;font-size:5px;font-weight:700;color:var(--brand-dark)}
.memo-fields{position:absolute;left:14px;top:52px;width:100px}
.memo-field{font-size:2.7px;border-bottom:.4px solid var(--rule);padding:2px 0 .6px;font-weight:600}
.memo-note{position:absolute;right:14px;top:89px;text-align:right;font-size:2.2px;line-height:3px;color:var(--ink-soft)}
.memo-greeting{position:absolute;left:14px;top:104px;font-size:2.8px;line-height:3.8px}
.memo-rule{position:absolute;left:14px;right:14px;bottom:10px;border-top:.4px solid var(--brand-red)}
.memo-contact{position:absolute;left:14px;right:14px;bottom:5px;display:flex;justify-content:space-between;font-size:2.1px;color:var(--ink-soft)}
</style>
</head>
<body>

<!-- Letterhead option 1 -->
<section class="sheet sheet--letter-1">
  <svg class="header-art" viewBox="0 0 172 40" aria-hidden="true"><path d="M0 0H172V19C120 15 60 18 0 30Z" fill="var(--brand-red)"/><path d="M0 30C60 18 120 15 172 19V22C120 19 60 23 0 34Z" fill="var(--brand-dark)"/></svg>
  <div class="brand"><span class="brand-square"></span>CORVANE ASSOCIATES</div>
  <div class="partners">Dana Whitlow, Managing Partner<br>Rhys Calder, Managing Partner<br>Mara Ellis, Associate Partner</div>
  <div class="ref">REF: #0370463</div>
  <div class="block tiny" style="top:46px">March 24, 2011<br><br><b>Mr. Owen Marsh</b><br>Managing Director<br>12 Harbour Road<br>Kingsford NSW 2032</div>
  <div class="block tiny" style="top:80px">
    <p class="para">Thank you for your recent enquiry. Our team has reviewed the matter and prepared the attached advice for your consideration. Please contact our office should you wish to discuss next steps.</p>
    <p class="para">Thank you for your recent enquiry. Our team has reviewed the matter and prepared the attached advice for your consideration. Please contact our office should you wish to discuss next steps.</p>
    <p class="para">Thank you for your recent enquiry. Our team has reviewed the matter and prepared the attached advice for your consideration. Please contact our office should you wish to discuss next steps.</p>
  </div>
  <div class="signoff tiny">Yours faithfully<br><br><br>Dana Whitlow<br>Managing Partner<br>dana@corvaneassociates.com.au</div>
  <div class="office">Level 4, 88 Collins Lane<br>Carrington NSW 2000<br>Ph +61 2 9000 1234<br>Fax +61 2 9000 1235</div>
  <svg class="footer-art" viewBox="0 0 172 8" preserveAspectRatio="none" aria-hidden="true"><rect y="3" width="172" height="5" fill="var(--brand-dark)"/><path d="M0 3H70L66 8H0Z" fill="var(--brand-red)"/></svg>
  <div class="web">www.corvaneassociates.com.au</div>
</section>
<div class="sheet-label" style="left:18px">Option-1</div>

<!-- Letterhead option 2 -->
<section class="sheet sheet--letter-2">
  <svg class="header-art" viewBox="0 0 172 40" aria-hidden="true"><path d="M0 0H172V19C120 15 60 18 0 30Z" fill="var(--brand-red)"/><path d="M0 30C60 18 120 15 172 19V22C120 19 60 23 0 34Z" fill="var(--brand-dark)"/></svg>
  <div class="brand"><span class="brand-square"></span>CORVANE ASSOCIATES</div>
  <div class="partners">Dana Whitlow, Managing Partner<br>Rhys Calder, Managing Partner<br>Mara Ellis, Associate Partner</div>
  <div class="ref">REF: #0370463</div>
  <div class="block tiny" style="top:46px">[Date]<br><br>[Name]<br>[Business]<br>[Address Line]<br>[ADDRESS LINE]</div>
  <div class="block tiny" style="top:80px">
    <p class="para">Thank you for your recent enquiry. Our team has reviewed the matter and prepared the attached advice for your consideration. Please contact our office should you wish to discuss next steps.</p>
    <p class="para">Thank you for your recent enquiry. Our team has reviewed the matter and prepared the attached advice for your consideration. Please contact our office should you wish to discuss next steps.</p>
    <p class="para">Thank you for your recent enquiry. Our team has reviewed the matter and prepared the attached advice for your consideration. Please contact our office should you wish to discuss next steps.</p>
  </div>
  <div class="signoff tiny">Yours faithfully<br><br><br>Dana Whitlow<br>Managing Partner<br>dana@corvaneassociates.com.au</div>
  <div class="office">Level 4, 88 Collins Lane<br>Carrington NSW 2000<br>Ph +61 2 9000 1234<br>Fax +61 2 9000 1235</div>
  <svg class="footer-art" viewBox="0 0 172 8" preserveAspectRatio="none" aria-hidden="true"><rect y="3" width="172" height="5" fill="var(--brand-dark)"/><path d="M0 3H70L66 8H0Z" fill="var(--brand-red)"/></svg>
  <div class="web">www.corvaneassociates.com.au</div>
</section>
<div class="sheet-label" style="left:207px">Option-2</div>

<!-- Facsimile -->
<section class="sheet sheet--fax">
  <svg class="header-art" viewBox="0 0 172 40" aria-hidden="true"><path d="M0 0H172V19C120 15 60 18 0 30Z" fill="var(--brand-red)"/><path d="M0 30C60 18 120 15 172 19V22C120 19 60 23 0 34Z" fill="var(--brand-dark)"/></svg>
  <div class="brand"><span class="brand-square"></span>CORVANE ASSOCIATES</div>
  <div class="partners">Dana Whitlow, Managing Partner<br>Rhys Calder, Managing Partner<br>Mara Ellis, Associate Partner</div>
  <h1 class="fax-title">FAX</h1>
  <div class="fax-grid">
    <div class="fax-field"><b>To:</b>(Recipient name)</div><div class="fax-field"><b>From:</b>(Your name)</div>
    <div class="fax-field"><b>Fax:</b>(Recipient fax number)</div><div class="fax-field"><b>Pages:</b>(Number of pages)</div>
    <div class="fax-field"><b>Phone:</b>(Recipient phone number)</div><div class="fax-field"><b>Date:</b>(Pick the date)</div>
    <div class="fax-field"><b>Re:</b>(Subject)</div><div class="fax-field"><b>CC:</b>(Name)</div>
  </div>
  <div class="fax-checks"><span>Urgent</span><span>For Review</span><span>Please Comment</span><span>Please Reply</span><span>Please Recycle</span></div>
  <div class="fax-greeting">Dear Sir,</div>
  <div class="block tiny" style="top:113px">
    <p class="para">Thank you for your recent enquiry. Our team has reviewed the matter and prepared the attached advice for your consideration. Please contact our office should you wish to discuss next steps.</p>
  </div>
  <div class="signoff tiny">Yours faithfully<br><br><br>Dana Whitlow<br>Managing Partner<br>dana@corvaneassociates.com.au</div>
  <div class="office">Level 4, 88 Collins Lane<br>Carrington NSW 2000<br>Ph +61 2 9000 1234<br>Fax +61 2 9000 1235</div>
  <svg class="footer-art" viewBox="0 0 172 8" preserveAspectRatio="none" aria-hidden="true"><rect y="3" width="172" height="5" fill="var(--brand-dark)"/><path d="M0 3H70L66 8H0Z" fill="var(--brand-red)"/></svg>
  <div class="web">www.corvaneassociates.com.au</div>
</section>
<div class="sheet-label" style="left:400px">Option-3</div>

<!-- Memo 1 -->
<section class="sheet sheet--memo-1">
  <svg class="header-art" viewBox="0 0 172 40" aria-hidden="true"><path d="M0 0H172V19C120 15 60 18 0 30Z" fill="var(--brand-red)"/><path d="M0 30C60 18 120 15 172 19V22C120 19 60 23 0 34Z" fill="var(--brand-dark)"/></svg>
  <div class="brand"><span class="brand-square"></span>CORVANE ASSOCIATES</div>
  <div class="partners">Dana Whitlow, Managing Partner<br>Rhys Calder, Managing Partner<br>Mara Ellis, Associate Partner</div>
  <div class="ref">REF: #0370463</div>
  <div class="memo-fields"><div class="memo-field">Date :</div><div class="memo-field">Name :</div><div class="memo-field">Business :</div><div class="memo-field">Address Line 1 :</div><div class="memo-field">Address Line 2 :</div></div>
  <div class="memo-note">Re: Matter Details Review &mdash; 3 Pages<br>Issued on 24.03.2011</div>
  <div class="memo-greeting">Dear Colleagues,<br>Re: Matter Details</div>
  <div class="signoff tiny">Yours faithfully<br><br><br>Dana Whitlow<br>Managing Partner<br>dana@corvaneassociates.com.au</div>
  <div class="office">Level 4, 88 Collins Lane<br>Carrington NSW 2000<br>Ph +61 2 9000 1234<br>Fax +61 2 9000 1235</div>
  <svg class="footer-art" viewBox="0 0 172 8" preserveAspectRatio="none" aria-hidden="true"><rect y="3" width="172" height="5" fill="var(--brand-dark)"/><path d="M0 3H70L66 8H0Z" fill="var(--brand-red)"/></svg>
  <div class="web">www.corvaneassociates.com.au</div>
</section>
<div class="sheet-label" style="left:598px">Memo-1</div>

<!-- Memo 2 -->
<section class="sheet sheet--memo-2">
  <svg class="header-art" viewBox="0 0 172 40" aria-hidden="true"><path d="M0 0H172V19C120 15 60 18 0 30Z" fill="var(--brand-red)"/><path d="M0 30C60 18 120 15 172 19V22C120 19 60 23 0 34Z" fill="var(--brand-dark)"/></svg>
  <div class="brand"><span class="brand-square"></span>CORVANE ASSOCIATES</div>
  <div class="partners">Dana Whitlow, Managing Partner<br>Rhys Calder, Managing Partner<br>Mara Ellis, Associate Partner</div>
  <div class="ref">REF: #0370463</div>
  <div class="memo-fields"><div class="memo-field">Date :</div><div class="memo-field">Name :</div><div class="memo-field">Business :</div><div class="memo-field">Address Line 1 :</div><div class="memo-field">Address Line 2 :</div></div>
  <div class="memo-note">Re: Matter Details Review &mdash; 3 Pages<br>Issued on 24.03.2011</div>
  <div class="memo-greeting">Dear Colleagues,<br>Re: Matter Details</div>
  <div class="signoff tiny">Yours faithfully<br><br><br>Dana Whitlow<br>Managing Partner<br>dana@corvaneassociates.com.au</div>
  <div class="memo-rule"></div>
  <div class="memo-contact"><span>Ph +61 2 9000 1234</span><span>Fax +61 2 9000 1235</span><span>www.corvaneassociates.com.au</span></div>
</section>
<div class="sheet-label" style="left:795px">Memo-2</div>

<!-- Memo 3 -->
<section class="sheet sheet--memo-3">
  <svg class="header-art" viewBox="0 0 172 40" aria-hidden="true"><rect x="0" y="26" width="172" height=".8" fill="var(--brand-red)"/></svg>
  <div class="brand" style="top:20px"><span class="brand-square"></span>CORVANE ASSOCIATES</div>
  <div class="partners">Dana Whitlow, Managing Partner<br>Rhys Calder, Managing Partner<br>Mara Ellis, Associate Partner</div>
  <div class="ref">REF: #0370463</div>
  <div class="memo-fields"><div class="memo-field">Date :</div><div class="memo-field">Name :</div><div class="memo-field">Business :</div><div class="memo-field">Address Line 1 :</div><div class="memo-field">Address Line 2 :</div></div>
  <div class="memo-note">Re: Matter Details Review &mdash; 3 Pages<br>Issued on 24.03.2011</div>
  <div class="memo-greeting">Dear Colleagues,<br>Re: Matter Details</div>
  <div class="signoff tiny">Yours faithfully<br><br><br>Dana Whitlow<br>Managing Partner<br>dana@corvaneassociates.com.au</div>
  <div class="memo-rule"></div>
  <div class="memo-contact"><span>Ph +61 2 9000 1234</span><span>Fax +61 2 9000 1235</span><span>www.corvaneassociates.com.au</span></div>
</section>
<div class="sheet-label" style="left:990px">Memo-3</div>

</body>
</html>
```